Brivora Collective Business Card Design

We need a business card design for Brivora Collective. We are a healthcare recruiting, wellness and education company. We partner with medical facilities to find quality candidates. We also offer free wellness courses.
The final design should communicate an emphasis on recruiting and wellness
The main purpose of the business card is to utilized it for networking events, give to hospitals, executives, VCs surgery centers and clinics. I want it to be sleek, clean, use of our brand colors and professional.

```html
<!DOCTYPE html>
<html lang="en">
<head>
<meta charset="utf-8">
<title>Brivora Collective Business Card</title>
<link rel="stylesheet" href="https://fonts.googleapis.com/css2?family=Questrial&display=swap">
<style>
  :root {
    --brand-green: #005c52;
    --paper: #ffffff;
    --stage: #e4e5e7;
    --photo-light: #f3f3f6;
    --photo-mid: #dcdde6;
    --photo-deep: #c9cbdb;
  }
  * { margin: 0; padding: 0; box-sizing: border-box; }
  html, body {
    width: 1200px; height: 1200px; overflow: hidden;
    background: var(--stage);
    font-family: "Questrial", "Century Gothic", sans-serif;
  }
  .sheet {
    position: relative; width: 1200px; height: 1200px;
  }
  .card {
    position: absolute; left: 140px; width: 920px; height: 525px; overflow: hidden;
  }
  .card--front { top: 50px; background: var(--paper); }
  .card--back { top: 625px; background: var(--brand-green); color: var(--paper); }

  .front-photo {
    position: absolute; inset: 0;
    background:
      radial-gradient(ellipse at 65% 55%, var(--photo-deep) 0%, transparent 45%),
      linear-gradient(90deg, var(--photo-light) 0%, var(--photo-mid) 55%, var(--photo-light) 100%);
    opacity: 0.75;
  }
  .front-brand {
    position: absolute; left: 175px; top: 118px;
    display: flex; align-items: center; gap: 28px;
    color: var(--brand-green);
  }
  .front-brand__square {
    width: 120px; height: 120px; background: var(--brand-green); border-radius: 10px;
  }
  .front-brand__name {
    font-size: 78px; line-height: 0.95; letter-spacing: -1px;
  }
  .web-band {
    position: absolute; left: 0; right: 0; top: 405px; height: 65px;
    background: var(--brand-green); color: var(--paper);
    display: flex; align-items: center; justify-content: center;
    font-size: 28px; letter-spacing: 1px; padding-right: 40px;
  }

  .back-mark {
    position: absolute; left: 600px; top: 60px; width: 270px;
    display: flex; flex-direction: column; align-items: center; gap: 22px;
  }
  .back-mark__square {
    width: 180px; height: 180px; background: var(--paper); border-radius: 14px;
  }
  .back-mark__name { font-size: 30px; text-align: center; }

  .holder {
    position: absolute; left: 52px; top: 222px;
  }
  .holder__name {
    font-size: 54px; letter-spacing: 1px; line-height: 1;
    padding-bottom: 8px; border-bottom: 2px solid var(--paper); display: inline-block;
  }
  .holder__role { font-size: 29px; margin-top: 18px; }
  .contact-list { list-style: none; margin-top: 24px; }
  .contact-list li {
    display: flex; align-items: center; gap: 18px;
    font-size: 29px; height: 41px; letter-spacing: 0.5px;
  }
  .contact-list svg { width: 22px; height: 22px; fill: var(--paper); flex: none; }
</style>
</head>
<body>
<main class="sheet">
  <section class="card card--front">
    <div class="front-photo" role="img" aria-label="Softly faded photo of healthcare staff walking through a bright hospital lobby"></div>
    <div class="front-brand">
      <div class="front-brand__square"></div>
      <div class="front-brand__name">Brivora<br>Collective</div>
    </div>
    <div class="web-band">www.brivoracollective.com</div>
  </section>

  <section class="card card--back">
    <div class="back-mark">
      <div class="back-mark__square"></div>
      <div class="back-mark__name">Brivora Collective</div>
    </div>
    <div class="holder">
      <h1 class="holder__name" style="font-weight:400">Name Surname</h1>
      <p class="holder__role">Position</p>
      <ul class="contact-list">
        <li>
          <svg viewBox="0 0 24 24" aria-hidden="true"><path d="M6.6 10.8a15.1 15.1 0 0 0 6.6 6.6l2.2-2.2a1 1 0 0 1 1-.25 11.4 11.4 0 0 0 3.6.57 1 1 0 0 1 1 1V20a1 1 0 0 1-1 1A17 17 0 0 1 3 4a1 1 0 0 1 1-1h3.5a1 1 0 0 1 1 1c0 1.25.2 2.45.57 3.57a1 1 0 0 1-.25 1z"/></svg>
          123 456 7890
        </li>
        <li>
          <svg viewBox="0 0 24 24" aria-hidden="true"><path d="M2 5h20v14H2z M3.5 6.5 12 13l8.5-6.5" fill="none" stroke="#fff" stroke-width="2"/></svg>
          name@brivoracollective.com
        </li>
        <li>
          <svg viewBox="0 0 24 24" aria-hidden="true"><path d="M5 2v18l5-4.5 3.5 7 2.7-1.3-3.4-6.9H19z"/></svg>
          www.brivoracollective.com
        </li>
      </ul>
    </div>
  </section>
</main>
</body>
</html>
```